Etiketten-Design für Kloster Likör
Zielgruppe
Wir sind ein katholisches Zisterzienserinnenkloster, das Menschen auf der Suche einen Ort der Stille und Erholung anbietet.
Unser Original Kloster Wendrup Kräuterlikör erlaubt es unseren Gästen einen Schluck Genuss von hier mitzunehmen.
Unsere Zielgruppe sind Frauen und Männer, die einen achtsamen Lebensstil schätzen.
Aufgabenstellung
Die klare Botschaft des Etiketts sollte sein: dieser Likör kommt aus dem Kloster Wendrup.
Gerne mit einem schön gestalteten Schriftzug, oder einem stilisierten Bildelement, das hohen Wiedererkennungswert hat. Hierfür eignen sich möglicherweise die drei Frauen auf dem Boot, die Kirchensilhouette, das Siegel oder der Kirchengiebel.
Farblich sollte es nicht zu grell oder bunt sein und zum Likör passen. Denkbar wäre z.B. ein schöner Grünton mit silbernen Akzenten.

```html
<!DOCTYPE html>
<html lang="de">
<head>
<meta charset="utf-8">
<title>Kräuterlikör – Etikett Kloster Wendrup</title>
<link rel="stylesheet" href="https://fonts.googleapis.com/css2?family=Oswald:wght@500&family=Barlow+Condensed:wght@400;500&display=swap">
<style>
  :root {
    --page: #f1f1f1;
    --paper-light: #f3ecd8;
    --paper-dark: #e2d5b4;
    --ink: #151515;
    --herb-green: #6b7f4e;
    --herb-green-deep: #4e6138;
    --title-green: #5a6e45;
    --rule: #26301e;
    --cream: #efe7cf;
    --figure-cream: #d9d2a8;
  }
  * { margin: 0; padding: 0; box-sizing: border-box; }
  html, body {
    width: 1200px; height: 848px; overflow: hidden;
    background: var(--page);
  }
  .label {
    position: absolute; left: 365px; top: 72px;
    width: 470px; height: 704px;
    background: radial-gradient(ellipse at 50% 35%, var(--paper-light) 0%, var(--paper-dark) 100%);
    overflow: hidden;
  }
  .ribbon {
    position: absolute; left: 187px; top: 0;
    width: 95px; height: 100px;
    background: var(--ink);
  }
  .seal-dot {
    position: absolute; left: 195px; top: 62px;
    width: 80px; height: 80px; border-radius: 50%;
    background: var(--ink);
    border: 4px solid var(--paper-light);
    box-shadow: 0 0 0 2px var(--ink);
  }
  .house-name {
    position: absolute; left: 0; right: 0; top: 160px;
    text-align: center;
    font-family: "Barlow Condensed", sans-serif; font-weight: 500;
    font-size: 20px; letter-spacing: 4px; text-transform: uppercase;
    color: var(--ink);
  }
  .product-title {
    position: absolute; left: 0; right: 0; top: 232px;
    text-align: center;
    font-family: "Oswald", sans-serif; font-weight: 500;
    font-size: 60px; letter-spacing: 3px; line-height: 1;
    color: var(--title-green);
  }
  .rule {
    position: absolute; left: 0; right: 0; height: 2px;
    background: var(--rule);
  }
  .rule--top { top: 309px; }
  .rule--bottom { top: 675px; }
  .herb-band {
    position: absolute; left: 0; right: 0; top: 314px; height: 358px;
    background: var(--herb-green);
  }
  .ingredients {
    position: absolute; left: 0; right: 0; top: 26px;
    text-align: center;
    font-family: "Barlow Condensed", sans-serif; font-weight: 500;
    font-size: 14px; letter-spacing: 1.2px; line-height: 17px;
    color: var(--cream);
  }
  .illustration {
    position: absolute; left: 0; right: 0; bottom: 0; height: 240px;
    background:
      radial-gradient(ellipse 22% 62% at 50% 68%, var(--figure-cream) 0%, rgba(217,210,168,0.55) 45%, rgba(217,210,168,0) 100%),
      linear-gradient(180deg, var(--herb-green) 0%, #61754a 55%, var(--herb-green-deep) 100%);
  }
  .volume {
    position: absolute; left: 32px; bottom: 6px;
    font-family: "Barlow Condensed", sans-serif; font-weight: 500;
    font-size: 14px; color: var(--cream);
  }
  .footer {
    position: absolute; left: 0; right: 0; top: 679px; height: 25px;
    background: var(--herb-green-deep);
    text-align: center;
    font-family: "Barlow Condensed", sans-serif; font-weight: 400;
    font-size: 11.5px; line-height: 25px; letter-spacing: 0.3px;
    color: var(--cream);
  }
</style>
</head>
<body>
  <article class="label">
    <div class="ribbon"></div>
    <div class="seal-dot"></div>
    <p class="house-name">Kloster Wendrup</p>
    <h1 class="product-title">KRÄUTERLIKÖR</h1>
    <div class="rule rule--top"></div>
    <section class="herb-band">
      <p class="ingredients">
        MELISSE · YSOPKRAUT · LAVENDEL · RINGELBLUME · BEIFUSS<br>
        KORIANDER · PFEFFERMINZE · ANGELIKAWURZEL
      </p>
      <div class="illustration" role="img" aria-label="Illustration: drei stilisierte Frauenfiguren zwischen Kräuterzweigen in Grün- und Cremetönen"></div>
      <p class="volume">0,5 l 35 % Vol.</p>
    </section>
    <div class="rule rule--bottom"></div>
    <footer class="footer">Kloster Wendrup GmbH Brunnenweg 12 · 39114 Marienfeld · ✆ 04561-228300</footer>
  </article>
</body>
</html>
```